Double and triple glazing window and door flyer

We are looking for an A4 leaflet which will fold into two advertising our products which are double glazed windows, doors and conservatories. It will have therefore, 4 A5 sides. Our website www.harbellhomecraft.co.uk shows the large range of products we offer.
The heading should read something like "Save money on double or triple glazing NOW". The banner we have for the company is "The best value tmoney can by" Our selling points are: Established since 1988. Family owned and run business which offers exceptional service. 10 year no-risk insured guarantees on all products. We have a range of designs, materials and glazing options for bespoke windows and doors to suit the age and style of your home; all with high security locking.
The latest most advance technology providing outstanding energy savings and sound reduction.
Full Members of the Allied Guild of Pane Fitters (see our website).
Call for a free quote now. Telephone 01632 960518
Text suggestion:
"We are a friendly, family- owned and run company which recognises that trust, integrity and good service are the key foundations for any business.

We offer expert advice, so that you may choose from a very large range of British Made windows, doors and conservatories produced from uPVC, aluminium, hardwood and composite materials: Products individually made from our extensive range to suit your home; whether modern or traditional. All our products are made to the highest standards. Installations are carried out by specialist tradesmen and conform to all Building Regulations."

Target Market(s)

Domestic householders

Font styles to use
Serif

Colors
3176b5
f04a50
33b8a4

Requirements
Must have
• Colourful and eye-catching. Reason to respond.Feel of quality ,reliability and good service
Nice to have
• Made in Britain marque.
• Awarded full membership of PRIME 50 Select Frame and Sunroom Fitters Society.
Should not have
• Discounts. Special offers.

```html
<!DOCTYPE html>
<html lang="en">
<head>
<meta charset="utf-8">
<title>Harbell – Double Glazing Leaflet</title>
<link href="https://fonts.googleapis.com/css2?family=PT+Serif&family=PT+Sans+Narrow:wght@400;700&family=Source+Sans+3:wght@400;600&display=swap" rel="stylesheet">
<style>
:root{
  --blue:#1f7fc4;
  --blue-dark:#1565a8;
  --blue-light:#36a6e0;
  --navy:#1d3b63;
  --seal-navy:#263f8a;
  --red:#d21f2b;
  --red-pill:#e0262f;
  --ink:#444;
  --grey-bg:#e6e6e6;
  --white:#fff;
}
*{margin:0;padding:0;box-sizing:border-box}
html,body{width:875px;height:1200px;overflow:hidden;background:var(--grey-bg)}
body{position:relative;font-family:"Source Sans 3",Arial,sans-serif;color:var(--ink)}
.spread{position:absolute;left:67px;width:750px;box-shadow:0 6px 8px rgba(0,0,0,.18)}
.spread--outer{top:36px;height:531px}
.spread--inner{top:610px;height:530px}
.page{position:absolute;top:0;width:375px;height:100%;overflow:hidden;background:var(--white)}
.page--left{left:0}
.page--right{left:375px}
.bg{position:absolute;inset:0}
.abs{position:absolute}
.photo{position:absolute}
.serif{font-family:"PT Serif",Georgia,serif}
.narrow{font-family:"PT Sans Narrow",Arial,sans-serif}

/* seal */
.seal{position:absolute;border-radius:50%;background:var(--white);border:4px solid var(--seal-navy);box-shadow:0 0 0 3px var(--white),0 2px 5px rgba(0,0,0,.35)}
.seal::before{content:"";position:absolute;inset:5px;border-radius:50%;border:1.5px dashed var(--seal-navy)}
.seal::after{content:"";position:absolute;inset:17px;border-radius:50%;background:radial-gradient(circle at 40% 38%,#e04a52,#b51d28 70%);border:2px solid var(--seal-navy)}

/* back cover */
.back-title{left:0;width:375px;top:40px;text-align:center;color:var(--red);font-size:24px;letter-spacing:.5px}
.back-sub{left:0;width:375px;top:77px;text-align:center;color:var(--white);font-size:15px}
.back-copy{left:19px;top:222px;width:282px;color:var(--white);font-size:10.5px;line-height:13px;letter-spacing:-.15px}
.back-copy p{margin-bottom:9px}
.cta{left:19px;top:388px;color:var(--white);font-size:13.5px;font-weight:700}
.pill{display:flex;align-items:center;justify-content:center;gap:6px;background:var(--red-pill);color:var(--white);border-radius:11px;font-size:14.5px;letter-spacing:2px;font-weight:600}
.back-pill{left:19px;top:408px;width:170px;height:20px}
.contacts{left:19px;top:448px;color:var(--white);font-size:9.5px;line-height:14px}
.contacts li{list-style:none;display:flex;align-items:flex-start;gap:7px}
.contacts .ic{width:9px;height:9px;background:var(--red-pill);border-radius:2px;margin-top:2px;flex:none}
.award{left:215px;top:437px;width:160px;font-size:5.8px;line-height:7px;text-align:center;color:#333}
.badges{left:228px;top:458px;width:138px;display:grid;grid-template-columns:repeat(4,1fr);gap:7px 5px}
.badge{height:17px;background:#d9d9d9;border-radius:2px}
.badge--blue{background:#5b8fc7}
.badge--red{background:#e57a3a}
.badge--dark{background:#555}
.badge--wide{grid-column:span 2}

/* front cover */
.front-title{left:0;width:375px;top:40px;text-align:center;color:var(--red);font-size:38px;letter-spacing:.5px;line-height:44px}
.front-sub{left:0;width:375px;top:84px;text-align:center;font-size:11.5px;color:#555}
.front-slogan{left:21px;top:443px;color:var(--navy);font-size:22px;line-height:28px}
.front-url{left:21px;top:500px;font-size:10.5px;color:#555}

/* inside left */
.in-head{left:18px;top:235px;color:var(--red);font-size:17px;line-height:23px;font-weight:400}
.in-copy{left:18px;top:285px;width:343px;font-size:10.5px;line-height:13px;text-align:justify;letter-spacing:-.15px}
.in-copy p{margin-bottom:7px}
.ticks li{list-style:none;position:relative;padding-left:16px;margin-bottom:8px;text-align:left}
.ticks svg{position:absolute;left:0;top:1px}
.values{left:0;width:375px;top:467px;text-align:center;color:var(--blue);font-size:11.5px;letter-spacing:.5px}
.band{left:0;width:375px;bottom:0;height:27px;background:linear-gradient(90deg,var(--blue-dark),var(--blue-light))}
.in-pill{left:113px;top:492px;width:190px;height:21px}

/* inside right */
.range-head{left:8px;top:185px;color:var(--red);font-size:12px;letter-spacing:-.2px}
.product{position:absolute;width:175px;height:60px}
.product svg{position:absolute;left:0;top:0}
.product h3{position:absolute;left:62px;top:0;font-weight:400;font-size:11px;color:var(--blue);border-bottom:1px solid #888;padding-bottom:1px;white-space:nowrap}
.product p{position:absolute;left:62px;top:18px;width:112px;font-size:7.3px;line-height:9.5px;color:#444}
.band-url{right:18px;bottom:7px;color:var(--white);font-size:11px}
</style>
</head>
<body>

<!-- OUTER SPREAD -->
<section class="spread spread--outer">
  <article class="page page--left">
    <svg class="bg" width="375" height="531" viewBox="0 0 375 531">
      <defs>
        <linearGradient id="backBlue" x1="0" y1="0" x2="1" y2="1">
          <stop offset="0" stop-color="#1a6fb4"/><stop offset="1" stop-color="#2d9ad8"/>
        </linearGradient>
      </defs>
      <rect width="375" height="531" fill="url(#backBlue)"/>
      <polygon points="0,0 95,0 0,140" fill="#195fa3" opacity=".6"/>
      <polygon points="300,0 375,0 375,260" fill="#3aa9e2" opacity=".35"/>
      <polygon points="0,110 60,110 0,210" fill="#3aa9e2" opacity=".35"/>
      <polygon points="150,531 375,531 375,270" fill="#fff"/>
    </svg>
    <div class="abs back-title serif">HARBELL</div>
    <div class="abs back-sub narrow">SAVE MONEY ON DOUBLE OR TRIPLE GLAZING NOW</div>
    <svg class="photo" style="left:0;top:111px" width="375" height="96" role="img" aria-label="Photographs of a white conservatory and open bi-fold patio doors">
      <defs>
        <linearGradient id="consGrad" x1="0" y1="0" x2="0" y2="1">
          <stop offset="0" stop-color="#a8c6de"/><stop offset=".45" stop-color="#eef1f2"/><stop offset=".75" stop-color="#b4684e"/><stop offset="1" stop-color="#7a8a5a"/>
        </linearGradient>
        <linearGradient id="doorGrad" x1="0" y1="0" x2="1" y2="0">
          <stop offset="0" stop-color="#c9b9a6"/><stop offset=".4" stop-color="#6f6358"/><stop offset=".7" stop-color="#d9d2c6"/><stop offset="1" stop-color="#a05a44"/>
        </linearGradient>
      </defs>
      <polygon points="8,96 55,0 215,0 168,96" fill="#fff"/>
      <polygon points="13,93 58,3 210,3 165,93" fill="url(#consGrad)"/>
      <polygon points="178,96 225,0 375,0 340,96" fill="#fff"/>
      <polygon points="183,93 228,3 370,3 337,93" fill="url(#doorGrad)"/>
    </svg>
    <div class="abs back-copy">
      <p>Established since 1988. Family owned and run business which offers exceptional service. 10 year no-risk insured guarantees on all products. We have a range of designs, materials and glazing options for bespoke windows and doors to suit the age and style of your home; all with high security locking.</p>
      <p>The latest most advance technology providing outstanding energy savings and sound reduction.</p>
      <p>Full Members of the Allied Guild of Pane Fitters</p>
    </div>
    <div class="abs cta narrow">CALL FOR A FREE QUOTE NOW</div>
    <div class="abs pill back-pill">
      <svg width="13" height="13" viewBox="0 0 24 24"><circle cx="12" cy="12" r="11" fill="none" stroke="#fff" stroke-width="2"/><path d="M8 6l2 0 1 3-1.5 1a7 7 0 0 0 4.5 4.5l1-1.5 3 1v2a2 2 0 0 1-2 2A10 10 0 0 1 6 8a2 2 0 0 1 2-2z" fill="#fff"/></svg>
      01632 960518
    </div>
    <ul class="abs contacts">
      <li><span class="ic"></span>01632 960518</li>
      <li><span class="ic"></span>harbell.home@postmail.co.uk</li>
      <li><span class="ic"></span>harbellhomecraft.co.uk</li>
      <li><span class="ic"></span><span>58 Linden Crescent<br>Westbury, WB4 2PL</span></li>
    </ul>
    <div class="abs award">Awarded full membership of PRIME 50 Select Frame and Sunroom Fitters Society.</div>
    <div class="abs badges">
      <span class="badge badge--blue"></span><span class="badge badge--red"></span><span class="badge"></span><span class="badge badge--dark"></span>
      <span class="badge"></span><span class="badge"></span><span class="badge badge--red badge--wide"></span>
    </div>
  </article>

  <article class="page page--right">
    <svg class="bg" width="375" height="531" viewBox="0 0 375 531">
      <polygon points="0,0 78,0 0,170" fill="#1f7fc4"/>
      <polygon points="0,0 40,0 0,90" fill="#1565a8"/>
      <polygon points="265,531 375,531 375,350" fill="#1f7fc4"/>
      <polygon points="325,531 375,531 375,440" fill="#36a6e0"/>
    </svg>
    <div class="abs front-title serif">HARBELL</div>
    <div class="abs front-sub narrow">DOUBLE GLAZED WINDOWS • DOORS • CONSERVATORIES</div>
    <div class="photo" style="left:0;top:111px;width:375px;height:299px;clip-path:polygon(48px 0,375px 0,375px 299px,0 299px,0 100px);background:linear-gradient(90deg,rgba(255,255,255,0) 55%,rgba(238,238,240,.55) 75%,rgba(220,224,232,.4) 100%),linear-gradient(180deg,#7fa9c9 0%,#9b6a55 18%,#a5503b 40%,#c6bdb3 62%,#b7aea4 80%,#6d6a66 100%)" role="img" aria-label="Photograph of a smiling family in front of a red-brick house with white windows"></div>
    <div class="seal" style="left:231px;top:364px;width:90px;height:90px"></div>
    <div class="abs front-slogan serif">THE BEST VALUE<br>MONEY CAN BUY</div>
    <div class="abs front-url">www.harbellhomecraft.co.uk</div>
  </article>
</section>

<!-- INNER SPREAD -->
<section class="spread spread--inner">
  <article class="page page--left">
    <div class="photo" style="left:0;top:0;width:375px;height:209px;background:linear-gradient(90deg,rgba(95,40,28,.25) 0%,rgba(240,240,236,.35) 50%,rgba(95,40,28,.25) 100%),linear-gradient(180deg,#7d3e2e 0%,#a4614b 30%,#d8d3cb 55%,#9a6450 75%,#5f7a4a 100%)" role="img" aria-label="Photograph of a brick house with white sash windows and French doors"></div>
    <svg class="abs" style="left:0;top:0" width="375" height="209">
      <polygon points="0,40 45,209 0,209" fill="#1f7fc4"/>
      <polygon points="0,0 50,0 0,110" fill="#36a6e0" opacity=".6"/>
      <polygon points="320,0 375,0 375,120" fill="#36a6e0" opacity=".8"/>
    </svg>
    <svg class="photo" style="left:0;top:148px" width="375" height="61" role="img" aria-label="Photographs of a brick bungalow, a white conservatory and a red front door">
      <defs>
        <linearGradient id="bungGrad" x1="0" y1="0" x2="0" y2="1"><stop offset="0" stop-color="#a9c3d8"/><stop offset=".4" stop-color="#9c5a45"/><stop offset="1" stop-color="#6c7a4c"/></linearGradient>
        <linearGradient id="consGrad2" x1="0" y1="0" x2="0" y2="1"><stop offset="0" stop-color="#5d7f58"/><stop offset=".5" stop-color="#e8ecea"/><stop offset="1" stop-color="#8a9a7a"/></linearGradient>
        <linearGradient id="doorGrad2" x1="0" y1="0" x2="1" y2="0"><stop offset="0" stop-color="#b06a55"/><stop offset=".5" stop-color="#c0242c"/><stop offset="1" stop-color="#a86250"/></linearGradient>
      </defs>
      <polygon points="10,61 35,0 150,0 125,61" fill="#fff"/>
      <polygon points="15,59 38,2 146,2 122,59" fill="url(#bungGrad)"/>
      <polygon points="130,61 155,0 260,0 235,61" fill="#fff"/>
      <polygon points="135,59 158,2 256,2 232,59" fill="url(#consGrad2)"/>
      <polygon points="240,61 265,0 375,0 375,61" fill="#fff"/>
      <polygon points="245,59 268,2 375,2 375,59" fill="url(#doorGrad2)"/>
    </svg>
    <h1 class="abs in-head serif">HARBELL<br>THE BEST VALUE MONEY CAN BUY</h1>
    <div class="abs in-copy">
      <p>We are a friendly, family- owned and run company which recognises that trust, integrity and good service are the key foundations for any business.</p>
      <p>We offer expert advice, so that you may choose from a very large range of British Made windows, doors and conservatories produced from uPVC, aluminium, hardwood and composite materials:</p>
      <ul class="ticks">
        <li><svg width="11" height="11" viewBox="0 0 11 11"><rect x=".5" y="1.5" width="9" height="9" fill="none" stroke="#1f7fc4"/><path d="M2.5 5.5l2 2 5-6" fill="none" stroke="#1f7fc4" stroke-width="1.5"/></svg>Products individually made from our extensive range to suit your home whether modern or traditional.</li>
        <li><svg width="11" height="11" viewBox="0 0 11 11"><rect x=".5" y="1.5" width="9" height="9" fill="none" stroke="#1f7fc4"/><path d="M2.5 5.5l2 2 5-6" fill="none" stroke="#1f7fc4" stroke-width="1.5"/></svg>All our products are made to the highest standards.</li>
        <li><svg width="11" height="11" viewBox="0 0 11 11"><rect x=".5" y="1.5" width="9" height="9" fill="none" stroke="#1f7fc4"/><path d="M2.5 5.5l2 2 5-6" fill="none" stroke="#1f7fc4" stroke-width="1.5"/></svg>Installations are carried out by specialist tradesmen and conform to all Building Regulations.</li>
      </ul>
    </div>
    <div class="abs values narrow">FEEL OF QUALITY &nbsp;• RELIABILITY &nbsp;• GOOD SERVICE</div>
    <div class="abs band"></div>
    <div class="abs pill in-pill">
      <svg width="13" height="13" viewBox="0 0 24 24"><circle cx="12" cy="12" r="11" fill="none" stroke="#fff" stroke-width="2"/><path d="M8 6l2 0 1 3-1.5 1a7 7 0 0 0 4.5 4.5l1-1.5 3 1v2a2 2 0 0 1-2 2A10 10 0 0 1 6 8a2 2 0 0 1 2-2z" fill="#fff"/></svg>
      01632 960518
    </div>
  </article>

  <article class="page page--right">
    <div class="photo" style="left:0;top:0;width:375px;height:172px;background:linear-gradient(90deg,rgba(120,60,40,.2) 0%,rgba(255,230,190,.15) 50%,rgba(70,150,190,.35) 100%),linear-gradient(180deg,#8a4c3a 0%,#a86a4a 22%,#c98f52 42%,#e2c08a 58%,#b07a4a 72%,#8c5a44 86%,#c9c2b8 100%)" role="img" aria-label="Photograph of a wood-effect Victorian conservatory on a brick base"></div>
    <svg class="abs" style="left:0;top:0" width="375" height="172">
      <polygon points="330,0 375,0 375,110" fill="#36a6e0" opacity=".85"/>
    </svg>
    <div class="seal" style="left:268px;top:124px;width:90px;height:90px"></div>
    <div class="abs range-head narrow">DOUBLE GLAZED WINDOWS • DOORS • CONSERVATORIES</div>

    <div class="product" style="left:18px;top:240px">
      <svg width="56" height="50" viewBox="0 0 62 54"><polygon points="16,1 46,1 61,27 46,53 16,53 1,27" fill="#fff" stroke="#1f7fc4" stroke-width="1.5"/><rect x="19" y="13" width="24" height="28" fill="none" stroke="#1f7fc4" stroke-width="2"/><line x1="31" y1="13" x2="31" y2="41" stroke="#1f7fc4" stroke-width="2"/></svg>
      <h3>uPVC Windows</h3>
      <p>• Casement Windows<br>• Tilt &amp; Turn Windows<br>• French Windows</p>
    </div>
    <div class="product" style="left:188px;top:240px">
      <svg width="56" height="50" viewBox="0 0 62 54"><polygon points="16,1 46,1 61,27 46,53 16,53 1,27" fill="#fff" stroke="#1f7fc4" stroke-width="1.5"/><rect x="22" y="10" width="18" height="34" fill="none" stroke="#1f7fc4" stroke-width="2"/><rect x="25" y="14" width="5" height="8" fill="#1f7fc4"/><rect x="32" y="14" width="5" height="8" fill="#1f7fc4"/><rect x="25" y="26" width="5" height="8" fill="#1f7fc4"/><rect x="32" y="26" width="5" height="8" fill="#1f7fc4"/></svg>
      <h3>Hardwood Doors</h3>
      <p>We offer front doors, back doors, double doors and patio doors in hardwood.</p>
    </div>
    <div class="product" style="left:18px;top:310px">
      <svg width="56" height="50" viewBox="0 0 62 54"><polygon points="16,1 46,1 61,27 46,53 16,53 1,27" fill="#fff" stroke="#1f7fc4" stroke-width="1.5"/><rect x="18" y="14" width="26" height="26" fill="none" stroke="#1f7fc4" stroke-width="2"/><line x1="31" y1="14" x2="31" y2="40" stroke="#1f7fc4" stroke-width="2"/><line x1="18" y1="27" x2="44" y2="27" stroke="#1f7fc4" stroke-width="2"/></svg>
      <h3>Hardwood Windows</h3>
      <p>• Traditional<br>• Contemporary</p>
    </div>
    <div class="product" style="left:188px;top:310px">
      <svg width="56" height="50" viewBox="0 0 62 54"><polygon points="16,1 46,1 61,27 46,53 16,53 1,27" fill="#fff" stroke="#1f7fc4" stroke-width="1.5"/><path d="M18 12l9 4v26l-9-4zM27 16h8v26h-8zM35 16l9-4v26l-9 4z" fill="none" stroke="#1f7fc4" stroke-width="2"/></svg>
      <h3>Folding &amp; sliding doors</h3>
      <p>• Patio or Sliding Doors<br>• Bi-fold Doors</p>
    </div>
    <div class="product" style="left:18px;top:369px">
      <svg width="56" height="50" viewBox="0 0 62 54"><polygon points="16,1 46,1 61,27 46,53 16,53 1,27" fill="#fff" stroke="#1f7fc4" stroke-width="1.5"/><rect x="22" y="10" width="18" height="34" fill="#1f7fc4"/><rect x="25" y="13" width="12" height="12" fill="#fff"/><circle cx="36" cy="30" r="1.5" fill="#fff"/></svg>
      <h3>Composite doors</h3>
      <p>All of our composite doors are manufactured to the highest quality standards.</p>
    </div>
    <div class="product" style="left:188px;top:369px">
      <svg width="56" height="50" viewBox="0 0 62 54"><polygon points="16,1 46,1 61,27 46,53 16,53 1,27" fill="#fff" stroke="#1f7fc4" stroke-width="1.5"/><path d="M14 26l17-14 17 14z" fill="#1f7fc4"/><rect x="16" y="28" width="30" height="14" fill="none" stroke="#1f7fc4" stroke-width="2"/><line x1="23" y1="28" x2="23" y2="42" stroke="#1f7fc4" stroke-width="2"/><line x1="31" y1="28" x2="31" y2="42" stroke="#1f7fc4" stroke-width="2"/><line x1="39" y1="28" x2="39" y2="42" stroke="#1f7fc4" stroke-width="2"/></svg>
      <h3>Conservatories</h3>
      <p>Garden Room, Victorian, Edwardian, Gable End, P Shaped, Bespoke Conservatory</p>
    </div>
    <div class="product" style="left:18px;top:434px">
      <svg width="56" height="50" viewBox="0 0 62 54"><polygon points="16,1 46,1 61,27 46,53 16,53 1,27" fill="#fff" stroke="#1f7fc4" stroke-width="1.5"/><path d="M22 44V16a9 9 0 0 1 18 0v28z" fill="#1f7fc4"/><rect x="26" y="18" width="4" height="8" fill="#fff"/><rect x="32" y="18" width="4" height="8" fill="#fff"/><rect x="26" y="30" width="4" height="8" fill="#fff"/><rect x="32" y="30" width="4" height="8" fill="#fff"/></svg>
      <h3>uPVC Doors</h3>
      <p>We have many different styles, colours and designs to choose from.</p>
    </div>
    <div class="product" style="left:188px;top:434px">
      <svg width="56" height="50" viewBox="0 0 62 54"><polygon points="16,1 46,1 61,27 46,53 16,53 1,27" fill="#fff" stroke="#1f7fc4" stroke-width="1.5"/><rect x="22" y="10" width="18" height="26" fill="none" stroke="#1f7fc4" stroke-width="2"/><rect x="18" y="34" width="26" height="9" fill="#8fc6e8" stroke="#1f7fc4"/></svg>
      <h3>Juliet Balconies</h3>
      <p>All Juliet Balconies have 10mm clear toughened glass; green, grey/bronze and blue tints.</p>
    </div>

    <div class="abs band"></div>
    <div class="abs band-url">www.harbellhomecraft.co.uk</div>
  </article>
</section>

</body>
</html>
```